Redesign Charity Golf Outing Flyer

We need a redesign of our current golf outing flyer. The charity is in the name of a fallen police officer and the funds help scholarships for future police officers and community projects. I have included the artwork from last year. We brand everything with "The Chief 417" because Derek's badge number was 417 and he often told people he was "the man". The details on the flyer will need to be editable (we have access to the full Adobe creative suite). While the cause is serious the event itself is fun so feel free to have fun with it.

Target Market(s)

Golfers and people who want to donate.

Industry/Entity Type

Charity

Font styles to use
Sans Serif

Colors
0555a3

Requirements
Must have
• All information included on last years flyer.
Nice to have
• A modern feel.
Should not have
• N/a

```html
<!DOCTYPE html>
<html lang="en">
<head>
<meta charset="utf-8">
<title>Derek D. Holloway Memorial &amp; Scholarship Golf Scramble</title>
<link rel="stylesheet" href="https://fonts.googleapis.com/css2?family=Anton&family=Open+Sans:wght@400;600;700&display=swap">
<style>
  :root {
    --brand-blue: #0555a3;
    --deep-blue: #0a2f7a;
    --bright-blue: #2a9be8;
    --sky: #dcefff;
    --orange: #f7941d;
    --gold: #ffc83d;
    --ink: #333a44;
    --white: #ffffff;
    --stage: #e9ecf0;
  }
  * { box-sizing: border-box; margin: 0; padding: 0; }
  html, body { width: 960px; height: 1200px; overflow: hidden; background: var(--stage); }
  body { font-family: "Open Sans", sans-serif; color: var(--ink); }

  .flyer {
    position: absolute; left: 30px; top: 18px; width: 900px; height: 1164px;
    background: linear-gradient(180deg, #eef7ff 0%, var(--sky) 100%);
    overflow: hidden; box-shadow: 0 6px 24px rgba(0,0,0,.18);
  }
  .hero {
    position: absolute; left: 0; top: 0; width: 900px; height: 724px;
    background:
      radial-gradient(circle at 78% 46%, #7fd0ff 0%, var(--bright-blue) 22%, var(--brand-blue) 48%, var(--deep-blue) 85%);
  }
  .hero::after {
    content: ""; position: absolute; left: 0; right: 0; bottom: 0;
    border-bottom: 2px dashed rgba(255,255,255,.7);
  }

  .title { position: absolute; left: 40px; top: 30px; color: var(--white);
    font-family: "Anton", sans-serif; line-height: 1; text-shadow: 0 3px 6px rgba(0,0,40,.45); }
  .title span { display: block; font-size: 70px; margin-bottom: 6px; letter-spacing: .5px; }

  .honoree-photo { position: absolute; left: 636px; top: 70px; width: 230px; height: 230px;
    border-radius: 50%; background: radial-gradient(circle at 50% 40%, #5b6470, #1b1f27 70%); }
  .honoree-name { position: absolute; left: 636px; top: 274px; width: 230px; text-align: center;
    font-family: "Anton", sans-serif; font-size: 34px; line-height: 1.1; color: var(--white); }

  .headline { position: absolute; left: 24px; top: 334px; font-family: "Anton", sans-serif;
    font-size: 132px; line-height: 1; letter-spacing: 1px;
    background: linear-gradient(180deg, var(--gold) 0%, var(--orange) 70%);
    -webkit-background-clip: text; background-clip: text; color: transparent;
    filter: drop-shadow(0 4px 4px rgba(0,0,40,.45)); }

  .venue { position: absolute; left: 44px; top: 490px; color: var(--white); font-size: 21px; line-height: 1.3; }
  .venue strong { font-weight: 700; }
  .schedule { position: absolute; left: 500px; top: 504px; color: var(--white); font-size: 20px; line-height: 1.3; }
  .schedule strong { font-weight: 700; }
  .schedule .note { font-size: 16px; }

  .pill { position: absolute; background: linear-gradient(180deg, #fff, #e7e7e7);
    border: 5px solid var(--orange); border-radius: 22px; padding: 9px 20px; color: var(--ink); }
  .pill strong { display: block; font-size: 18px; font-weight: 700; white-space: nowrap; }
  .pill span { font-size: 15px; white-space: nowrap; }
  .pill-register { left: 40px; top: 620px; width: 370px; }
  .pill-fee { left: 480px; top: 628px; width: 390px; }

  .form { position: absolute; left: 40px; top: 742px; width: 470px; font-size: 15px; }
  .form h2 { font-size: 18px; font-weight: 700; margin-bottom: 6px; }
  .field { display: flex; align-items: flex-end; height: 28px; }
  .field .line { flex: 1; border-bottom: 1.5px solid var(--ink); margin-left: 4px; height: 18px; }
  .field .gap { width: 14px; }
  .deadline { margin-top: 10px; font-size: 16px; line-height: 1.35; }
  .deadline strong { font-weight: 700; }
  .payable { font-weight: 700; font-size: 15px; }
  .mail-bar { margin-top: 6px; background: var(--brand-blue); color: var(--white); font-size: 16px; padding: 2px 12px; }

  .sponsor-box { position: absolute; left: 520px; top: 766px; width: 350px; height: 230px; }
  .sponsor-box svg { position: absolute; inset: 0; }
  .sponsor-text { position: absolute; left: 30px; top: 16px; width: 296px; font-size: 14px; line-height: 1.35; }
  .sponsor-text h3 { font-size: 18px; font-weight: 700; line-height: 1.25; margin-bottom: 2px; }
  .sponsor-text small { font-size: 12px; }
  .sponsor-text .blank { border-bottom: 1.5px solid var(--ink); height: 26px; margin-bottom: 6px; }
  .sponsor-text .field { height: 26px; }

  .contact { position: absolute; left: 560px; top: 1016px; font-size: 15px; line-height: 1.45; }
  .contact h3 { font-size: 18px; font-weight: 700; margin-bottom: 10px; }
</style>
</head>
<body>
<main class="flyer">
  <section class="hero">
    <h1 class="title">
      <span>2nd Annual</span>
      <span>Derek D. Holloway</span>
      <span>Memorial &amp;</span>
      <span>Scholarship</span>
    </h1>
    <div class="honoree-photo" role="img" aria-label="Portrait of the honoured officer in uniform"></div>
    <div class="honoree-name">The Chief 417</div>
    <div class="headline">GOLF SCRAMBLE</div>

    <div class="venue">
      <strong>Cedar Ridge Golf Course</strong><br>
      1450 Birchwood Avenue Rd.<br>
      Fairview, OH 44810<br>
      (555) 201-3344
    </div>
    <div class="schedule">
      <strong>Saturday — August</strong><br>
      9:00 am Registration<br>
      <span class="note">Day of Scramble Registrations are welcome</span><br>
      <strong>10:00 am ShotGun Start</strong>
    </div>

    <div class="pill pill-register">
      <strong>Register below or Online at:</strong>
      <span>www.417golf.eventreg.com</span>
    </div>
    <div class="pill pill-fee">
      <strong>Entry Fee: $55/Person ($220/Team)</strong>
      <span>Includes Green fees, cart and dinner</span>
    </div>
  </section>

  <section class="form">
    <h2>Team Captian Information:</h2>
    <div class="field">Captain’s Name:<span class="line"></span></div>
    <div class="field">Address:<span class="line"></span></div>
    <div class="field">City:<span class="line"></span><span class="gap"></span>State:<span class="line"></span><span class="gap"></span>Zip:<span class="line"></span></div>
    <div class="field">Captain’s Phone:<span class="line"></span></div>
    <div class="field">Captain’s Email:<span class="line"></span></div>
    <div class="field">Player # 2 Name:<span class="line"></span></div>
    <div class="field">Player # 3 Name:<span class="line"></span></div>
    <div class="field">Player # 4 Name:<span class="line"></span></div>
    <p class="deadline"><strong>Mail-in Deadline: August 1, 2015</strong><br>
      Mail this completed from with check(s) made Payable to:<br>
      <span class="payable">“The Office Derek D. Holloway Memorial Scholarship Fund”</span></p>
    <div class="mail-bar">Mail to contact information on the right.</div>
  </section>

  <section class="sponsor-box">
    <svg width="350" height="230" viewBox="0 0 350 230" aria-hidden="true">
      <path d="M24 4 H326 Q346 4 346 24 V172 Q346 192 326 192 H60 L8 226 L20 190 Q4 186 4 170 V24 Q4 4 24 4 Z"
            fill="#ffffff" stroke="#0555a3" stroke-width="7"/>
    </svg>
    <div class="sponsor-text">
      <h3>Can’t Make it or Don’t Golf?<br>Sponsor a hole/tee:</h3>
      Name/Business<br>
      <small>(attached business card if possible):</small>
      <div class="blank"></div>
      <div class="field">Donation Amount:<span class="line"></span></div>
    </div>
  </section>

  <section class="contact">
    <h3>Any Questions Contact:</h3>
    Dale Whitman<br>
    782 Maple Grove Lane<br>
    Lakeview, OH 44812<br>
    (555) 418-2290
  </section>
</main>
</body>
</html>
```